New Business Card Design Project

Use the flyer uploaded and website www.brightoakbuilders.com for inspiration.
List Our Services on Backside of business cards
Martin Hollis
Harborline Renovations Inc.
Licensed General Contractors
858-471-9063

Contact Information for Business Card

Use the flyer uploaded and website www.brightoakbuilders.com for inspiration. List Our Services on Backside of business cards Martin Hollis Harborline Renovations Inc. Licensed General Contractors 858-471-9063

```html
<!DOCTYPE html>
<html lang="en">
<head>
<meta charset="utf-8">
<title>Harborline Renovations – Business Cards</title>
<link rel="stylesheet" href="https://fonts.googleapis.com/css2?family=Lato:wght@400;700;900&family=Oswald:wght@500;600&display=swap">
<style>
  :root {
    --bg: #2a2c30;
    --card: #0e0e0f;
    --ink: #f4f4f4;
    --ink-soft: #c9c9c9;
    --rule: #e6e6e6;
    --shadow: rgba(0,0,0,0.55);
  }
  * { box-sizing: border-box; margin: 0; padding: 0; }
  html, body { width: 1200px; height: 900px; overflow: hidden; }
  body {
    background: var(--bg);
    font-family: "Lato", sans-serif;
    color: var(--ink);
    position: relative;
  }
  .card {
    position: absolute;
    left: 300px;
    width: 600px;
    height: 343px;
    background: var(--card);
    border-radius: 22px;
    box-shadow: 0 18px 40px var(--shadow);
    overflow: hidden;
  }
  .card--front { top: 72px; }
  .card--back { top: 475px; }

  .brand-name {
    font-family: "Lato", sans-serif;
    font-weight: 400;
    text-transform: uppercase;
    letter-spacing: 3px;
    color: var(--ink-soft);
    font-size: 22px;
    white-space: nowrap;
  }

  /* Front */
  .card--front .brand-name { position: absolute; left: 48px; top: 44px; }
  .person {
    position: absolute; left: 48px; top: 104px;
  }
  .person__name {
    font-weight: 900; font-size: 34px; letter-spacing: 0.5px; line-height: 1.1;
  }
  .person__role {
    font-weight: 700; font-size: 17px; margin-top: 6px;
  }
  .person__rule {
    width: 160px; height: 1.5px; background: var(--rule); margin-top: 12px;
  }
  .contact {
    position: absolute; left: 48px; top: 228px;
    list-style: none;
  }
  .contact__item {
    display: flex; align-items: center; gap: 12px;
    font-size: 17px; color: var(--ink-soft); margin-bottom: 12px;
  }
  .contact__icon { width: 16px; height: 16px; flex: none; }

  /* Back */
  .card--back .brand-name {
    position: absolute; left: 0; right: 0; top: 40px; text-align: center;
  }
  .services-head {
    position: absolute; left: 40px; right: 40px; top: 104px;
    display: flex; align-items: center; gap: 18px;
  }
  .services-head__rule { flex: 1; height: 1.5px; background: var(--rule); }
  .services-head__title {
    font-family: "Oswald", sans-serif; font-weight: 600; font-size: 22px;
    letter-spacing: 0.5px; text-transform: uppercase;
  }
  .services {
    position: absolute; left: 48px; right: 40px; top: 160px;
    display: flex; justify-content: space-between;
  }
  .services__list { list-style: none; }
  .services__item {
    display: flex; align-items: center; gap: 9px;
    font-family: "Oswald", sans-serif; font-weight: 500; font-size: 18px;
    margin-bottom: 14px;
  }
  .tick { width: 15px; height: 15px; flex: none; }
</style>
</head>
<body>

<svg width="0" height="0" style="position:absolute">
  <defs>
    <symbol id="tick" viewBox="0 0 16 16">
      <rect x="1" y="1" width="14" height="14" fill="none" stroke="#f4f4f4" stroke-width="1.6"/>
      <path d="M4 8.3l2.8 2.8L12 5" fill="none" stroke="#f4f4f4" stroke-width="1.8"/>
    </symbol>
  </defs>
</svg>

<section class="card card--front" aria-label="Business card front">
  <div class="brand-name">Harborline Renovations</div>

  <div class="person">
    <h1 class="person__name">Martin Hollis</h1>
    <p class="person__role">Licensed General Contractors</p>
    <div class="person__rule"></div>
  </div>

  <ul class="contact">
    <li class="contact__item">
      <svg class="contact__icon" viewBox="0 0 16 16" aria-hidden="true">
        <path d="M4 1.5l2.2 3-1.4 1.6a9 9 0 0 0 5.1 5.1l1.6-1.4 3 2.2-1.3 2.5C7.6 14.4 1.6 8.4 1.5 2.8z" fill="#f4f4f4"/>
      </svg>
      <span>858-471-9063</span>
    </li>
    <li class="contact__item">
      <svg class="contact__icon" viewBox="0 0 16 16" aria-hidden="true">
        <circle cx="8" cy="8" r="6.8" fill="none" stroke="#f4f4f4" stroke-width="1.4"/>
        <ellipse cx="8" cy="8" rx="3" ry="6.8" fill="none" stroke="#f4f4f4" stroke-width="1.2"/>
        <path d="M1.2 8h13.6M2.5 4.5h11M2.5 11.5h11" stroke="#f4f4f4" stroke-width="1.1"/>
      </svg>
      <span>www.brightoakbuilders.com</span>
    </li>
  </ul>
</section>

<section class="card card--back" aria-label="Business card back">
  <div class="brand-name">Harborline Renovations</div>

  <div class="services-head">
    <span class="services-head__rule"></span>
    <h2 class="services-head__title">Our Services</h2>
    <span class="services-head__rule"></span>
  </div>

  <div class="services">
    <ul class="services__list">
      <li class="services__item"><svg class="tick"><use href="#tick"/></svg>Remodel: Kitchen &amp; Bath</li>
      <li class="services__item"><svg class="tick"><use href="#tick"/></svg>Painting: Interior &amp; Exterior</li>
      <li class="services__item"><svg class="tick"><use href="#tick"/></svg>Flooring: Carpet, Vinyl, Wood</li>
      <li class="services__item"><svg class="tick"><use href="#tick"/></svg>Window &amp; Door Replacement</li>
    </ul>
    <ul class="services__list">
      <li class="services__item"><svg class="tick"><use href="#tick"/></svg>Plumbing: Repairs &amp; Upgrades</li>
      <li class="services__item"><svg class="tick"><use href="#tick"/></svg>Energy-Efficient Upgrades</li>
      <li class="services__item"><svg class="tick"><use href="#tick"/></svg>Deck &amp; Patio Construction</li>
    </ul>
  </div>
</section>

</body>
</html>
```